Bath Salt Packaging

Hello! We are Dr Pelvo Organics, a company providing the best and most nutritious food and health-care products for the health conscious around the world!
We are currently in the process of releasing a few new products, one of which is Himalayan Bath Salt Crystals. It is an ancient, pure salt which has been protected from environmental toxins and pollution under the Himalayan mountains for more than 250 million years!
Our salt is 100% pure and unrefined, still containing the original mineral composition of the ancient life-giving ocean that supported our early ancestors. There are over 60 trace minerals in this salt, the majority of which exist in colloidal forms, meaning they are highly bioavailable and quickly ionized when added to water.
So, we need packaging designed for our four salt packets; a 300mL jar, a 150mL jar, a 10g sachet and a box which will house the sachets. I have attached the label content, measurements and a little extra instruction/information.
We want a natural, eco-friendly feel for the packaging. Thanks!
ps. please use the 3rd of the Logo's (TM, 'Organics' under leaf)

```html
<!DOCTYPE html>
<html lang="en">
<head>
<meta charset="utf-8">
<title>Dr Pelvo Organics – Himalayan Bath Salt Crystals Label</title>
<link href="https://fonts.googleapis.com/css2?family=Kaushan+Script&family=Oswald:wght@500;700&display=swap" rel="stylesheet">
<style>
  :root {
    --paper: #ffffff;
    --ink-dark: #2e2e2e;
    --forest: #1f4a2c;
    --leaf: #6aac2f;
    --leaf-deep: #559a22;
    --leaf-pale: #e6f2d6;
    --salt-pink: #e9a58b;
    --salt-light: #f6d3c2;
    --wood: #d8d4cf;
    --white: #ffffff;
  }
  html, body {
    margin: 0;
    padding: 0;
    overflow: hidden;
    background: var(--paper);
  }
  .label {
    position: relative;
    width: 1078px;
    height: 1200px;
    overflow: hidden;
    background: var(--paper);
  }
  .salt-photo {
    position: absolute;
    left: 0;
    top: 480px;
    width: 1078px;
    height: 720px;
    background:
      radial-gradient(ellipse 420px 300px at 440px 420px, var(--salt-pink) 0%, var(--salt-light) 55%, rgba(246,211,194,0) 100%),
      linear-gradient(to bottom, var(--paper) 0%, var(--wood) 45%, #c9c4be 100%);
  }
  .brand-name {
    position: absolute;
    top: 95px;
    left: 0;
    width: 1078px;
    text-align: center;
    margin: 0;
    font-family: "Kaushan Script", cursive;
    font-weight: 400;
    font-size: 92px;
    line-height: 1;
    color: var(--ink-dark);
  }
  .product-origin {
    position: absolute;
    top: 285px;
    left: 0;
    width: 1078px;
    text-align: center;
    margin: 0;
    font-family: "Kaushan Script", cursive;
    font-size: 88px;
    line-height: 1.1;
    color: var(--forest);
  }
  .product-name {
    position: absolute;
    top: 392px;
    left: 0;
    width: 1078px;
    margin: 0;
    text-align: center;
    font-family: "Oswald", sans-serif;
    font-weight: 500;
    font-size: 128px;
    line-height: 118px;
    letter-spacing: 6px;
    color: var(--leaf);
    text-transform: uppercase;
  }
  .ribbon {
    position: absolute;
    left: 0;
    top: 1062px;
    width: 400px;
    height: 92px;
  }
  .ribbon-text {
    position: absolute;
    left: 24px;
    top: 1072px;
    font-family: "Kaushan Script", cursive;
    font-size: 46px;
    color: var(--white);
    transform: rotate(-4deg);
  }
  .net-weight {
    position: absolute;
    left: 462px;
    top: 1062px;
    font-family: "Oswald", sans-serif;
    font-weight: 700;
    font-size: 62px;
    color: var(--white);
  }
  .values-seal {
    position: absolute;
    left: 668px;
    top: 795px;
    width: 364px;
    height: 364px;
  }
  .seal-words {
    font-family: "Oswald", sans-serif;
    font-weight: 500;
    font-size: 31px;
    letter-spacing: 1px;
    fill: var(--white);
  }
</style>
</head>
<body>
<div class="label">
  <div class="salt-photo" role="img" aria-label="Pink Himalayan salt crystals piled on a pale wooden surface"></div>

  <h1 class="brand-name">Dr Pelvo Organics</h1>
  <p class="product-origin">Himalayan</p>
  <h2 class="product-name">Bath Salt<br>Crystals</h2>

  <svg class="ribbon" viewBox="0 0 400 92" aria-hidden="true">
    <path d="M0 22 L380 4 L352 44 L392 80 L0 90 Z" fill="var(--leaf-deep)"/>
  </svg>
  <span class="ribbon-text">100% Natural</span>

  <span class="net-weight">150g</span>

  <svg class="values-seal" viewBox="0 0 364 364" aria-label="Organic, Ecofriendly, Fair trading, Healthy, Sustainable">
    <defs>
      <path id="seal-arc" d="M182 182 m-142 0 a142 142 0 1 1 284 0 a142 142 0 1 1 -284 0"/>
    </defs>
    <circle cx="182" cy="182" r="180" fill="var(--leaf)"/>
    <circle cx="182" cy="182" r="176" fill="none" stroke="var(--white)" stroke-width="3"/>
    <text class="seal-words">
      <textPath href="#seal-arc" startOffset="0">Sustainable • Organic • Ecofriendly • Fair trading • Healthy •</textPath>
    </text>
    <circle cx="182" cy="182" r="116" fill="var(--white)"/>
    <circle cx="182" cy="182" r="106" fill="var(--leaf-pale)" role="img" aria-label="Portrait of the company doctor in a white coat"/>
  </svg>
</div>
</body>
</html>
```